依頼詳細
当事務所は日本一敷居の低い事務所をめざしておりますので、固い弁護士をイメージさせるものではなく、親しみや遊び心があり、お気軽にお電話いただけるpopの作成をお願いいたします。
もっとも、整骨院の患者様、整骨院の経営者様の双方にご信頼いただけるpopの作成をお願いいたします。
記載項目
■代表弁護士の写真の掲載(添付資料、複数のうちから1枚選んでください。)
■代表弁護士氏名(添付資料)
■法律事務所名、事務所所在地、電話番号の記載(添付資料)
■「東雲弁護士会所属」との記載
■「日本一敷居の低い弁護士事務所」、もしくはそれをよりキャッチーに表現したものの記載
希望イメージ
シンプル 複雑
単色 カラフル
暗い 明るい
日常 高級
遊び心 厳粛
未来的 伝統的
女性的 男性的
希望する色
黄 緑 青 オレンジ
納品ファイル
• 高解像度JPG (.jpg)
• イラストレーター形式 (.ai)
補足説明
■大きさは、230mm×330mm程度のものでお願いいたします。
■大きさの範囲内であれば、形はどのようなものでも構いません。
■提案の段階では高解像度JPGで、納品はイラストレーター形式でお願いいたします。
■何かご質問がございましたら、ぜひお尋ねください。

事務所職員で当選を選んだのですが、写真に写る者の雰囲気とデザインから感じられる雰囲気がとてもマッチしていたこと、遊び心あるデザインがとても気に入りました。

どのご提案も素晴らしかったです。
ありがとうございました。

```html
<!DOCTYPE html>
<html lang="ja">
<head>
<meta charset="utf-8">
<title>ひかり法律事務所 POP</title>
<link rel="stylesheet" href="https://fonts.googleapis.com/css2?family=Noto+Sans+JP:wght@500;700;900&display=swap">
<style>
  :root {
    --red: #e60012;
    --ink: #1a1a1a;
    --blue: #1460b8;
    --blue-deep: #0d4a94;
    --yellow: #ffe100;
    --white: #ffffff;
    --paper: #ffffff;
    --photo-a: #d9dde3;
    --photo-b: #3b4250;
    --illust-a: #f3e2cf;
    --illust-b: #5c7fa6;
  }
  * { box-sizing: border-box; margin: 0; padding: 0; }
  html, body { width: 836px; height: 1200px; overflow: hidden; background: var(--paper); }
  body { font-family: "Noto Sans JP", sans-serif; color: var(--ink); }

  .pop {
    position: relative;
    width: 836px;
    height: 1200px;
    background: var(--paper);
    border-radius: 40px;
    overflow: hidden;
  }

  .lawyer-photo {
    position: absolute;
    left: 0; top: 0;
    width: 490px; height: 840px;
    background: linear-gradient(160deg, var(--photo-a) 0%, #b9bfc9 35%, var(--photo-b) 100%);
    -webkit-mask-image: linear-gradient(90deg, #000 65%, transparent 100%);
            mask-image: linear-gradient(90deg, #000 65%, transparent 100%);
  }

  .tagline {
    position: absolute;
    right: 70px; top: 26px;
    color: var(--red);
    font-weight: 900;
    font-size: 46px;
    line-height: 1.3;
    letter-spacing: 0.06em;
  }
  .tagline span { display: block; }
  .tagline .line-1 { padding-left: 24px; }

  .headline {
    position: absolute;
    left: 276px; top: 252px;
    width: 530px;
    font-weight: 900;
    text-align: center;
    white-space: nowrap;
  }
  .headline span { display: block; }
  .headline .top {
    position: relative;
    font-size: 118px;
    line-height: 1.0;
    letter-spacing: 0.02em;
    padding-left: 20px;
  }
  .headline .top .sun {
    position: absolute;
    left: 26px; top: 10px;
    width: 92px; height: 92px;
    border-radius: 50%;
    background: var(--red);
  }
  .headline .top .word { position: relative; display: inline; }
  .headline .middle { font-size: 70px; line-height: 1.1; margin-top: 6px; }
  .headline .bottom { font-size: 80px; line-height: 1.05; letter-spacing: -0.01em; }

  .question {
    position: absolute;
    left: 468px; top: 548px;
    font-weight: 700;
    font-size: 23px;
    line-height: 1.35;
    color: var(--ink);
  }
  .question .lead { color: var(--red); font-size: 21px; display: block; transform: skewX(-8deg); }

  .staff-illustration {
    position: absolute;
    left: 640px; top: 640px;
    width: 170px; height: 200px;
    border-radius: 85px 85px 10px 10px;
    background: linear-gradient(180deg, var(--illust-a) 0%, var(--illust-a) 40%, var(--illust-b) 100%);
  }

  .call-burst {
    position: absolute;
    left: 448px; top: 700px;
    width: 190px; height: 140px;
  }
  .call-burst svg { width: 100%; height: 100%; display: block; }
  .call-burst .text {
    position: absolute;
    inset: 0;
    display: flex; flex-direction: column; justify-content: center; align-items: center;
    color: var(--red);
    font-weight: 900;
    font-size: 26px;
    line-height: 1.15;
    transform: rotate(-8deg);
  }

  .office-band {
    position: absolute;
    left: 0; top: 840px;
    width: 836px; height: 360px;
    background: var(--blue);
    color: var(--white);
    border-radius: 0 0 40px 40px;
  }
  .office-band .membership {
    position: absolute;
    left: 40px; top: 14px;
    font-weight: 900;
    font-size: 50px;
    letter-spacing: 0.02em;
  }
  .office-band .office-name {
    position: absolute;
    left: 36px; top: 76px;
    font-weight: 900;
    font-size: 84px;
    letter-spacing: 0.02em;
    line-height: 1.1;
    white-space: nowrap;
  }
  .office-band .address {
    position: absolute;
    left: 40px; top: 170px;
    font-weight: 700;
    font-size: 21px;
    letter-spacing: 0.02em;
    white-space: nowrap;
  }

  .phone-strip {
    position: absolute;
    left: 20px; top: 202px;
    width: 796px; height: 82px;
    background: var(--white);
    border-radius: 8px;
    display: flex; align-items: center;
    padding-left: 16px;
    color: var(--blue);
    font-weight: 900;
    white-space: nowrap;
  }
  .phone-strip .label { font-size: 58px; letter-spacing: -0.02em; margin-right: 8px; }
  .phone-strip .number { font-size: 76px; letter-spacing: 0.01em; }

  .representative {
    position: absolute;
    left: 20px; top: 296px;
    width: 796px; height: 44px;
    background: var(--white);
    border-radius: 6px;
    display: flex; align-items: center; justify-content: center;
    color: var(--blue-deep);
    font-weight: 700;
    font-size: 20px;
    letter-spacing: 0.08em;
  }
</style>
</head>
<body>
  <main class="pop">
    <div class="lawyer-photo" role="img" aria-label="代表弁護士の上半身写真（スーツ姿、目に炎の演出）"></div>

    <p class="tagline">
      <span class="line-1">あなたの為に</span>
      <span class="line-2">闘志燃やします。</span>
    </p>

    <h1 class="headline">
      <span class="top"><span class="sun" aria-hidden="true"></span><span class="word">日本一</span></span>
      <span class="middle">敷居の低い</span>
      <span class="bottom">弁護士事務所</span>
    </h1>

    <p class="question">
      <span class="lead">例えば</span>
      交通事故に合っちゃった<br>
      どうすればいいの??
    </p>

    <div class="staff-illustration" role="img" aria-label="困った表情で考え込む女性のイラスト"></div>

    <div class="call-burst">
      <svg viewBox="0 0 180 130" preserveAspectRatio="none" aria-hidden="true">
        <polygon fill="#ffe100" stroke="#e60012" stroke-width="2"
          points="178,65 158,77 166,97 139,99 134,120 108,111 90,128 72,111 46,120 41,99 14,97 22,77 2,65 22,53 14,34 41,31 46,10 72,19 90,2 108,19 134,10 139,31 166,34 158,53"/>
      </svg>
      <p class="text"><span>お気軽に</span><span>お電話</span><span>下さい!!</span></p>
    </div>

    <section class="office-band">
      <p class="membership">東雲弁護士会所属</p>
      <p class="office-name">ひかり法律事務所</p>
      <p class="address">〒530-0000 東雲市北区中央１丁目２番３号　東雲中央ビル４階</p>
      <p class="phone-strip"><span class="label">TEL</span><span class="number">(06)6000-1234</span></p>
      <p class="representative">代表弁護士：森川 健一</p>
    </section>
  </main>
</body>
</html>
```